The Christian Teacher Life-Cycle

Look at the Lifecyle of the Christian School.
Look at the BLT logo.
I am looking for a Christian Teacher Lifecycle that represents the slides in the PP upload.
Our website is bramblewoodlearningtrust.org.
The design should include a summary design showing all four stages, and then four slides representing each of the stages as subsets of the summary design.
When a teacher is going through the Lifecycle, they are going on their Professional Learning Journey that takes 40 years to unfold.
All five should include a copyright 2026 BLT on them.

```html
<!DOCTYPE html>
<html lang="en">
<head>
<meta charset="utf-8">
<title>Christian Teacher Professional Learning Journey – BLT</title>
<link href="https://fonts.googleapis.com/css2?family=Noto+Sans:wght@400;600;700;800&family=Montserrat:wght@500;600;700&display=swap" rel="stylesheet">
<style>
:root{
  --navy:#10294a;
  --navy-deep:#0b2140;
  --green:#3c6a35;
  --teal:#195e6c;
  --gold:#c6922c;
  --gold-light:#e0b55a;
  --ink:#27313f;
  --muted:#5a6472;
  --paper:#f7f5f0;
  --card:#ffffffee;
}
*{box-sizing:border-box;margin:0;padding:0}
html,body{width:1200px;height:660px;overflow:hidden;background:#ffffff}
body{font-family:"Noto Sans",sans-serif;color:var(--ink);position:relative}

/* ---------- summary hero ---------- */
.hero{position:absolute;left:10px;top:4px;width:1180px;height:349px;overflow:hidden;box-shadow:0 1px 4px #0002;background:var(--paper)}
.hero-scene{position:absolute;inset:0 0 28px 0;
  background:
   radial-gradient(ellipse 260px 200px at 960px 120px,#fff6dccc,transparent 70%),
   linear-gradient(160deg,transparent 40%,#5d5a4a55 70%,#3d3c33aa 100%),
   linear-gradient(90deg,#f8f6f1 0%,#f1ede4 30%,#d8d1c0 55%,#c9b894 75%,#e9d8ae 100%);}
.brand{position:absolute;left:40px;top:26px;display:flex;align-items:center;gap:7px}
.brand-mark{width:26px;height:26px;background:var(--navy);border-radius:4px}
.brand-name{font-family:"Noto Sans",sans-serif;font-weight:700;color:var(--navy);font-size:30px;line-height:1}
.brand-full{position:absolute;left:73px;top:56px;font-size:6px;letter-spacing:.8px;color:var(--navy);font-weight:600;text-transform:uppercase}
.brand-motto{position:absolute;left:34px;top:76px;font-size:6px;font-weight:700;color:var(--navy);letter-spacing:.3px}
.hero-title{position:absolute;left:38px;top:90px;font-weight:800;color:var(--navy);font-size:34px;line-height:1.05;letter-spacing:-.5px}
.hero-sub{position:absolute;left:39px;top:128px;font-weight:700;color:var(--green);font-size:22.5px;letter-spacing:-.2px}
.gold-rule{position:absolute;height:2px;background:var(--gold)}
.hero .gold-rule{left:40px;top:162px;width:36px}
.hero-kicker{position:absolute;left:40px;top:173px;font-family:"Montserrat",sans-serif;font-weight:500;font-size:10.5px;letter-spacing:2.4px;color:var(--navy);line-height:1.5}
.hero-quote{position:absolute;left:42px;top:221px;border-left:1.5px solid var(--gold);padding-left:15px;font-size:8.3px;line-height:1.42;color:var(--ink);width:190px}

.stage-pin{position:absolute;text-align:center;transform:translateX(-50%)}
.stage-pin .label{font-family:"Montserrat",sans-serif;font-weight:700;font-size:9px;letter-spacing:1px;color:var(--navy)}
.stage-pin .name{font-weight:700;font-size:12.5px;line-height:1.15;margin-top:2px}
.stage-pin svg{display:block;margin:4px auto 0}
.pin-1 .name{color:var(--navy)}
.pin-2 .name{color:var(--green)}
.pin-3 .name{color:var(--teal)}
.pin-4 .label,.pin-4 .name{color:var(--gold)}

.hero-years{position:absolute;left:933px;top:172px;color:#fff;text-shadow:0 1px 3px #0004}
.hero-years .t{font-size:16px;line-height:1.1}
.hero-years .bar{width:83px;height:1.5px;background:var(--gold-light);margin:8px 0 4px}
.hero-years .num{font-family:"Montserrat",sans-serif;font-weight:500;font-size:52px;color:var(--gold-light);line-height:1}
.hero-years .num small{font-family:"Noto Sans",sans-serif;font-size:17px;color:#fff;margin-left:4px;vertical-align:4px}

.hero-band{position:absolute;left:0;bottom:0;width:100%;height:28px;background:var(--navy-deep);border-top:2px solid var(--gold);display:flex;align-items:center;justify-content:center;gap:12px;color:#fff;font-family:"Montserrat",sans-serif;font-weight:600;font-size:9.5px;letter-spacing:1.8px}
.hero-band .dot{color:var(--gold)}
.hero-band .copy{position:absolute;right:38px;font-family:"Noto Sans",sans-serif;font-weight:400;letter-spacing:0;font-size:8.5px}

/* ---------- stage slides ---------- */
.slide{position:absolute;top:364px;width:287px;height:286px;overflow:hidden;background:var(--paper);box-shadow:0 1px 3px #0002}
.s1{left:10px}.s2{left:304px}.s3{left:597px}.s4{left:889px}
.slide-scene{position:absolute;inset:0 0 12px 0}
.s1 .slide-scene{background:radial-gradient(ellipse 130px 90px at 90px 230px,#6e8f4a88,transparent 70%),linear-gradient(180deg,#f7f6f2 0%,#eef0ee 45%,#c8ccc4 75%,#7b6a52 100%)}
.s2 .slide-scene{background:radial-gradient(ellipse 150px 80px at 110px 210px,#7a8c7a99,transparent 70%),linear-gradient(180deg,#f6f6f3 0%,#dfe4e0 45%,#9aa89a 75%,#6f8a8c 100%)}
.s3 .slide-scene{background:radial-gradient(ellipse 90px 70px at 143px 50px,#5b7a4acc,transparent 70%),linear-gradient(180deg,#f2f3f1 0%,#e7ebe6 40%,#f3f3f0 100%)}
.s4 .slide-scene{background:radial-gradient(ellipse 120px 160px at 120px 120px,#fff3d0,transparent 70%),linear-gradient(180deg,#efe6d2 0%,#dcc49a 50%,#a8824f 85%,#8a6a40 100%)}

.mini-brand{position:absolute;left:12px;top:6px;display:flex;align-items:center;gap:4px}
.mini-brand .brand-mark{width:13px;height:13px;border-radius:2px}
.mini-brand .brand-name{font-size:14px}
.mini-motto{position:absolute;left:13px;top:33px;font-size:4.4px;line-height:1.3;font-weight:600;color:var(--navy);text-transform:uppercase}
.slide-stage{position:absolute;left:13px;top:60px;font-family:"Montserrat",sans-serif;font-weight:700;font-size:8px;letter-spacing:.8px;color:var(--navy)}
.slide-title{position:absolute;left:12px;top:71px;font-weight:700;font-size:15.5px;line-height:1.07}
.slide .gold-rule{left:13px;top:112px;width:20px;height:1.5px}
.s1 .slide-title{color:var(--navy)}
.s2 .slide-title{color:var(--green)}
.s3 .slide-title{color:var(--teal)}
.s4 .slide-title,.s4 .slide-stage{color:var(--gold)}

.cards{position:absolute;list-style:none;display:flex;flex-direction:column;gap:5px}
.s1 .cards{left:153px;top:36px;width:120px}
.s2 .cards{left:149px;top:35px;width:128px}
.s4 .cards{left:165px;top:33px;width:113px;gap:4px}
.card{background:var(--card);border-radius:3px;box-shadow:0 0.5px 2px #0002;display:flex;align-items:center;gap:6px;padding:4px 5px;min-height:30px}
.s4 .card{min-height:34px}
.card .ico{flex:none;width:24px;height:24px;border-radius:50%;display:flex;align-items:center;justify-content:center}
.s1 .ico{background:var(--navy)}
.s2 .ico{background:var(--green)}
.s4 .card .ico{background:transparent;width:22px}
.card strong{display:block;font-size:5.8px;font-weight:700;color:var(--navy);line-height:1.2}
.s2 .card strong{color:var(--navy)}
.s4 .card strong{color:var(--gold)}
.card span{display:block;font-size:5px;color:var(--muted);line-height:1.3}

.cols{position:absolute;left:6px;top:121px;width:276px;display:flex;gap:5px}
.col{flex:1;background:#ffffffe6;border-radius:3px;padding:5px 5px 6px}
.col h3{font-family:"Montserrat",sans-serif;font-size:5.2px;font-weight:700;color:var(--teal);letter-spacing:.2px;margin-bottom:4px}
.col ul{list-style:none;display:flex;flex-direction:column;gap:4px}
.col li{display:flex;gap:5px;font-size:5px;line-height:1.3;color:var(--ink);align-items:flex-start}
.col li svg{flex:none;margin-top:1px}

.badge{position:absolute;left:50%;bottom:20px;transform:translateX(-50%);width:34px;height:34px;border-radius:50%;border:2px solid #fff;display:flex;align-items:center;justify-content:center;box-shadow:0 1px 3px #0003}
.s2 .badge{background:var(--green)}
.s3 .badge{background:var(--teal);bottom:18px;width:30px;height:30px}
.s4 .badge{background:var(--gold)}

.slide-foot{position:absolute;left:0;bottom:0;width:100%;height:12px;background:var(--navy-deep);color:#fff;font-size:4.6px;letter-spacing:.6px;font-weight:600;display:flex;align-items:center;justify-content:center;gap:6px}
.slide-foot .copy{position:absolute;right:12px;font-weight:400;letter-spacing:0}
</style>
</head>
<body>

<svg width="0" height="0" style="position:absolute" aria-hidden="true">
  <defs>
    <symbol id="i-sprout" viewBox="0 0 24 24"><path d="M12 21V11M12 12C12 7 8 5 4 5c0 4 3 7 8 7zM12 12c0-5 4-7 8-7 0 4-3 7-8 7z" fill="none" stroke="currentColor" stroke-width="1.6"/></symbol>
    <symbol id="i-people" viewBox="0 0 24 24"><g fill="none" stroke="currentColor" stroke-width="1.5"><circle cx="7" cy="8" r="2.5"/><circle cx="12" cy="7" r="2.5"/><circle cx="17" cy="8" r="2.5"/><path d="M3 18c0-4 2-6 4-6s4 2 4 6M8 18c0-5 2-7 4-7s4 2 4 7M13 18c0-4 2-6 4-6s4 2 4 6"/></g></symbol>
    <symbol id="i-bird" viewBox="0 0 24 24"><path d="M3 12c4 0 6-3 6-7 2 2 3 5 3 7 2-3 5-4 9-4-2 3-4 6-8 7l-2 4-2-3c-3 0-5-2-6-4z" fill="none" stroke="currentColor" stroke-width="1.5" stroke-linejoin="round"/></symbol>
    <symbol id="i-sun" viewBox="0 0 24 24"><g stroke="currentColor" stroke-width="1.4" fill="none"><circle cx="12" cy="12" r="3"/><path d="M12 2v6M12 16v6M2 12h6M16 12h6M5 5l4 4M15 15l4 4M19 5l-4 4M9 15l-4 4"/></g></symbol>
    <symbol id="i-person" viewBox="0 0 24 24"><g fill="none" stroke="currentColor" stroke-width="1.6"><circle cx="12" cy="8" r="4"/><path d="M4 21c0-5 4-7 8-7s8 2 8 7"/></g></symbol>
    <symbol id="i-board" viewBox="0 0 24 24"><g fill="none" stroke="currentColor" stroke-width="1.6"><rect x="3" y="4" width="18" height="12"/><path d="M8 20l4-4 4 4M7 12l3-3 3 2 4-4"/></g></symbol>
    <symbol id="i-book" viewBox="0 0 24 24"><path d="M3 5h7a2 2 0 0 1 2 2v13a2 2 0 0 0-2-2H3zM21 5h-7a2 2 0 0 0-2 2v13a2 2 0 0 1 2-2h7z" fill="none" stroke="currentColor" stroke-width="1.6"/></symbol>
    <symbol id="i-pencil" viewBox="0 0 24 24"><path d="M4 20l2-6L16 4l4 4-10 10zM14 6l4 4" fill="none" stroke="currentColor" stroke-width="1.6"/></symbol>
    <symbol id="i-head" viewBox="0 0 24 24"><g fill="none" stroke="currentColor" stroke-width="1.6"><path d="M8 21v-4c-3-1-4-4-4-7a8 8 0 0 1 16 0c0 2-1 3 0 5h-2v4h-4v2"/><circle cx="12" cy="10" r="2.5"/></g></symbol>
    <symbol id="i-check" viewBox="0 0 24 24"><g fill="none" stroke="currentColor" stroke-width="1.6"><rect x="4" y="3" width="16" height="18" rx="1"/><path d="M8 9l2 2 4-4M8 16h8"/></g></symbol>
    <symbol id="i-heart" viewBox="0 0 24 24"><path d="M12 20S3 14 3 8a4.5 4.5 0 0 1 9-1 4.5 4.5 0 0 1 9 1c0 6-9 12-9 12z" fill="none" stroke="currentColor" stroke-width="1.5"/></symbol>
    <symbol id="i-star" viewBox="0 0 24 24"><path d="M12 3l2.7 6 6.3.6-4.8 4.3 1.4 6.4L12 17l-5.6 3.3 1.4-6.4L3 9.6 9.3 9z" fill="none" stroke="currentColor" stroke-width="1.5" stroke-linejoin="round"/></symbol>
    <symbol id="i-dot" viewBox="0 0 10 10"><circle cx="5" cy="5" r="3.6" fill="none" stroke="currentColor" stroke-width="1.2"/></symbol>
  </defs>
</svg>

<!-- ===== Summary ===== -->
<section class="hero">
  <div class="hero-scene" role="img" aria-label="Sunlit mountain landscape with a winding path climbing to a summit where a teacher stands"></div>

  <div class="brand"><span class="brand-mark"></span><span class="brand-name">BLT</span></div>
  <div class="brand-full">Bramblewood<br>Learning Trust</div>
  <div class="brand-motto">FOR JESUS • THROUGH MISSION • WITH CHILDREN</div>

  <h1 class="hero-title">Christian Teacher</h1>
  <h2 class="hero-sub">Professional Learning Journey</h2>
  <div class="gold-rule"></div>
  <p class="hero-kicker">A 40-YEAR JOURNEY<br>OF PROFESSIONAL GROWTH</p>
  <p class="hero-quote">All are good.<br>The only sin is not growing.<br>It is a 40 year career-long<br>Professional Learning Journey.<br>I want to grow so that children<br>and teenagers will become<br>more than before.</p>

  <div class="stage-pin pin-1" style="left:472px;top:148px">
    <div class="label">STAGE 1</div><div class="name">Growing<br>Myself</div>
    <svg width="54" height="128" viewBox="0 0 54 128"><circle cx="27" cy="26" r="24" fill="var(--navy)" stroke="#fff" stroke-width="2"/><use href="#i-sprout" x="15" y="14" width="24" height="24" color="#fff"/><line x1="27" y1="50" x2="27" y2="121" stroke="var(--navy)" stroke-width="1.5"/><ellipse cx="27" cy="122" rx="8" ry="3.5" fill="var(--navy)"/></svg>
  </div>
  <div class="stage-pin pin-2" style="left:617px;top:90px">
    <div class="label">STAGE 2</div><div class="name">Growing<br>Together</div>
    <svg width="54" height="120" viewBox="0 0 54 120"><circle cx="27" cy="26" r="24" fill="var(--green)" stroke="#fff" stroke-width="2"/><use href="#i-people" x="13" y="12" width="28" height="28" color="#fff"/><line x1="27" y1="50" x2="27" y2="113" stroke="var(--green)" stroke-width="1.5"/><ellipse cx="27" cy="114" rx="8" ry="3.5" fill="var(--green)"/></svg>
  </div>
  <div class="stage-pin pin-3" style="left:778px;top:51px">
    <div class="label">STAGE 3</div><div class="name">Growing<br>Others</div>
    <svg width="54" height="100" viewBox="0 0 54 100"><circle cx="27" cy="26" r="24" fill="var(--teal)" stroke="#fff" stroke-width="2"/><use href="#i-bird" x="14" y="13" width="26" height="26" color="#fff"/><line x1="27" y1="50" x2="27" y2="93" stroke="var(--teal)" stroke-width="1.5"/><ellipse cx="27" cy="94" rx="7" ry="3" fill="var(--teal)"/></svg>
  </div>
  <div class="stage-pin pin-4" style="left:899px;top:20px">
    <div class="label">STAGE 4</div><div class="name">Transforming<br>Lives</div>
    <svg width="54" height="86" viewBox="0 0 54 86"><circle cx="27" cy="26" r="24" fill="var(--gold)" stroke="#fff" stroke-width="2"/><use href="#i-sun" x="14" y="13" width="26" height="26" color="#fff"/><line x1="27" y1="50" x2="27" y2="80" stroke="var(--gold)" stroke-width="1.5"/><ellipse cx="27" cy="81" rx="7" ry="3" fill="var(--gold)"/></svg>
  </div>

  <div class="hero-years">
    <div class="t">Professional<br>Learning Journey</div>
    <div class="bar"></div>
    <div class="num">40<small>YEARS</small></div>
  </div>

  <div class="hero-band">FOR JESUS <span class="dot">•</span> THROUGH MISSION <span class="dot">•</span> WITH CHILDREN<span class="copy">© 2026 BLT</span></div>
</section>

<!-- ===== Stage 1 ===== -->
<section class="slide s1">
  <div class="slide-scene" role="img" aria-label="Young green seedling growing from soil with misty mountains behind"></div>
  <div class="mini-brand"><span class="brand-mark"></span><span class="brand-name">BLT</span></div>
  <div class="mini-motto">For Jesus<br>Through Mission<br>With Children</div>
  <div class="slide-stage">STAGE 1</div>
  <h3 class="slide-title">Growing<br>Myself</h3>
  <div class="gold-rule"></div>
  <ul class="cards">
    <li class="card"><span class="ico"><svg width="14" height="14" color="#fff"><use href="#i-person"/></svg></span><div><strong>Self-Awareness</strong><span>The focus is on “I”</span></div></li>
    <li class="card"><span class="ico"><svg width="14" height="14" color="#fff"><use href="#i-board"/></svg></span><div><strong>Classroom Foundations</strong><span>Fundamental skills such as classroom management</span></div></li>
    <li class="card"><span class="ico"><svg width="14" height="14" color="#fff"><use href="#i-book"/></svg></span><div><strong>Curriculum Focus</strong><span>Curriculum is where I spend my time</span></div></li>
    <li class="card"><span class="ico"><svg width="14" height="14" color="#fff"><use href="#i-pencil"/></svg></span><div><strong>Learning Mindset</strong><span>I am a sponge rather than a contributor</span></div></li>
    <li class="card"><span class="ico"><svg width="14" height="14" color="#fff"><use href="#i-head"/></svg></span><div><strong>Reflection</strong><span>I reflect on my practice</span></div></li>
  </ul>
  <div class="slide-foot">FOR JESUS • THROUGH MISSION • WITH CHILDREN<span class="copy">© 2026 BLT</span></div>
</section>

<!-- ===== Stage 2 ===== -->
<section class="slide s2">
  <div class="slide-scene" role="img" aria-label="Old stone arch bridge over a river among misty forested hills"></div>
  <div class="mini-brand"><span class="brand-mark"></span><span class="brand-name">BLT</span></div>
  <div class="mini-motto">For Jesus<br>Through Mission<br>With Children</div>
  <div class="slide-stage">STAGE 2</div>
  <h3 class="slide-title">Growing<br>Together</h3>
  <div class="gold-rule"></div>
  <ul class="cards">
    <li class="card"><span class="ico"><svg width="15" height="15" color="#fff"><use href="#i-people"/></svg></span><div><strong>Christian Learning Community</strong><span>A place where I give and take</span></div></li>
    <li class="card"><span class="ico"><svg width="15" height="15" color="#fff"><use href="#i-people"/></svg></span><div><strong>We Over I</strong><span>I recognize that “we” is more powerful for the child than “I”</span></div></li>
    <li class="card"><span class="ico"><svg width="14" height="14" color="#fff"><use href="#i-book"/></svg></span><div><strong>Pedagogy Focus</strong><span>I know my curriculum – I am more focused on how</span></div></li>
    <li class="card"><span class="ico"><svg width="14" height="14" color="#fff"><use href="#i-check"/></svg></span><div><strong>Effective Assessment</strong><span>I assess relevant and effective tools</span></div></li>
    <li class="card"><span class="ico"><svg width="14" height="14" color="#fff"><use href="#i-head"/></svg></span><div><strong>Reflection</strong><span>I reflect on my practice</span></div></li>
  </ul>
  <div class="badge"><svg width="20" height="20" color="#fff"><use href="#i-people"/></svg></div>
  <div class="slide-foot">FOR JESUS • THROUGH MISSION • WITH CHILDREN<span class="copy">© 2026 BLT</span></div>
</section>

<!-- ===== Stage 3 ===== -->
<section class="slide s3">
  <div class="slide-scene" role="img" aria-label="Large tree on a hilltop with winding paths and birds in flight"></div>
  <div class="mini-brand"><span class="brand-mark"></span><span class="brand-name">BLT</span></div>
  <div class="mini-motto">For Jesus<br>Through Mission<br>With Children</div>
  <div class="slide-stage">STAGE 3</div>
  <h3 class="slide-title">Growing<br>Others</h3>
  <div class="gold-rule"></div>
  <div class="cols">
    <div class="col">
      <h3>A.&nbsp; LEADERSHIP WITH COLLEAGUES</h3>
      <ul>
        <li><svg width="8" height="8" color="var(--teal)"><use href="#i-person"/></svg>I lead in my Christian Professional Learning Community</li>
        <li><svg width="8" height="8" color="var(--teal)"><use href="#i-people"/></svg>Ensuring my colleagues continue to grow</li>
        <li><svg width="8" height="8" color="var(--teal)"><use href="#i-star"/></svg>We are humble in understanding where we still need to go</li>
        <li><svg width="8" height="8" color="var(--teal)"><use href="#i-person"/></svg>My colleagues see me as an important resource</li>
        <li><svg width="8" height="8" color="var(--teal)"><use href="#i-person"/></svg>I am a master of growth</li>
        <li><svg width="8" height="8" color="var(--teal)"><use href="#i-head"/></svg>I help my colleagues reflect</li>
      </ul>
    </div>
    <div class="col">
      <h3>B.&nbsp; EMPOWERING OUR STUDENTS</h3>
      <ul>
        <li><svg width="8" height="8" color="var(--teal)"><use href="#i-person"/></svg>I position the child as the owner of their learning</li>
        <li><svg width="8" height="8" color="var(--teal)"><use href="#i-star"/></svg>I give up control so the child can gain control</li>
        <li><svg width="8" height="8" color="var(--teal)"><use href="#i-board"/></svg>The child becomes an architect in their curriculum</li>
        <li><svg width="8" height="8" color="var(--teal)"><use href="#i-people"/></svg>The child becomes a collaborator in the how</li>
        <li><svg width="8" height="8" color="var(--teal)"><use href="#i-person"/></svg>I am more a learner than a teacher</li>
        <li><svg width="8" height="8" color="var(--teal)"><use href="#i-sun"/></svg>I am a master of pedagogies</li>
        <li><svg width="8" height="8" color="var(--teal)"><use href="#i-head"/></svg>I reflect on my practice through the eyes of children</li>
      </ul>
    </div>
  </div>
  <div class="badge"><svg width="18" height="18" color="#fff"><use href="#i-bird"/></svg></div>
  <div class="slide-foot">FOR JESUS • THROUGH MISSION • WITH CHILDREN<span class="copy">© 2026 BLT</span></div>
</section>

<!-- ===== Stage 4 ===== -->
<section class="slide s4">
  <div class="slide-scene" role="img" aria-label="Teacher standing on a golden sunlit path with children walking toward a village"></div>
  <div class="mini-brand"><span class="brand-mark"></span><span class="brand-name">BLT</span></div>
  <div class="mini-motto">For Jesus<br>Through Mission<br>With Children</div>
  <div class="slide-stage">STAGE 4</div>
  <h3 class="slide-title">Transforming<br>Lives</h3>
  <div class="gold-rule"></div>
  <ul class="cards">
    <li class="card"><span class="ico"><svg width="20" height="20" color="var(--gold)"><use href="#i-people"/></svg></span><div><strong>Transformational Leadership</strong><span>Comfortable making the child owner and leading colleagues</span></div></li>
    <li class="card"><span class="ico"><svg width="18" height="18" color="var(--gold)"><use href="#i-heart"/></svg></span><div><strong>Students Thrive</strong><span>Children come to and stay because I am there</span></div></li>
    <li class="card"><span class="ico"><svg width="18" height="18" color="var(--gold)"><use href="#i-star"/></svg></span><div><strong>Every Child Succeeds</strong><span>I want and work to ensure that every child succeeds</span></div></li>
    <li class="card"><span class="ico"><svg width="20" height="20" color="var(--gold)"><use href="#i-people"/></svg></span><div><strong>Every Colleague Succeeds</strong><span>I want and work to ensure that every colleague succeeds</span></div></li>
    <li class="card"><span class="ico"><svg width="18" height="18" color="var(--gold)"><use href="#i-book"/></svg></span><div><strong>Mastery</strong><span>Master of several pedagogies and of metacognition</span></div></li>
    <li class="card"><span class="ico"><svg width="18" height="18" color="var(--gold)"><use href="#i-person"/></svg></span><div><strong>Lifelong Learner</strong><span>I see myself as a learner<br>I reflect on my practice with my children / teens</span></div></li>
  </ul>
  <div class="badge"><svg width="20" height="20" color="#fff"><use href="#i-sun"/></svg></div>
  <div class="slide-foot">FOR JESUS • THROUGH MISSION • WITH CHILDREN<span class="copy">© 2026 BLT</span></div>
</section>

</body>
</html>
```